wig manufacturer
I would like something very upscale.highend looking
maybe mat chrome card with shiney chrome
or something like the Quince business card very clean and simple white with the logo in silver
Target Market(s)
upscale women
Industry/Entity Type
Business
Contact Information for Business Card
OUR LOGO
company name:Rosamund Wigs
48E92Avenue Harold Pinsett
Larkhaven,N.Y 10990
Tel:212-5550148
1800-5550193
email:tressline@mailbox.example
website:Rosamundwigs.example

```html
<!DOCTYPE html>
<html lang="en">
<head>
<meta charset="utf-8">
<title>Rosamund Wigs – Business Card</title>
<link rel="stylesheet" href="https://fonts.googleapis.com/css2?family=Questrial&display=swap">
<style>
  :root {
    --backdrop: #3b1216;
    --card: #ffffff;
    --ink: #8c8c8c;
    --silver-light: #e6e6e6;
    --silver-dark: #9a9a9a;
    --shadow: rgba(0, 0, 0, 0.45);
  }
  html, body {
    margin: 0;
    width: 1200px;
    height: 800px;
    overflow: hidden;
    background: var(--backdrop);
  }
  .canvas {
    position: relative;
    width: 1200px;
    height: 800px;
  }
  .business-card {
    position: absolute;
    left: 150px;
    top: 143px;
    width: 900px;
    height: 514px;
    background: var(--card);
    box-shadow: 0 18px 40px var(--shadow);
    font-family: "Questrial", "Century Gothic", sans-serif;
    color: var(--ink);
  }
  .brand {
    position: absolute;
    left: 56px;
    top: 48px;
    display: flex;
    align-items: center;
    gap: 14px;
  }
  .brand-dot {
    width: 22px;
    height: 22px;
    border-radius: 50%;
    background: linear-gradient(135deg, var(--silver-light), var(--silver-dark));
  }
  .brand-name {
    font-size: 30px;
    letter-spacing: 0.5px;
    color: var(--ink);
  }
  .contact {
    position: absolute;
    left: 56px;
    bottom: 52px;
    margin: 0;
    font-style: normal;
    font-size: 24px;
    line-height: 1.2;
  }
  .contact span { display: block; }
</style>
</head>
<body>
  <main class="canvas">
    <section class="business-card" aria-label="Rosamund Wigs business card">
      <div class="brand">
        <span class="brand-dot" aria-hidden="true"></span>
        <span class="brand-name">rosamund</span>
      </div>
      <address class="contact">
        <span>Tel: 212-5550148</span>
        <span>Tel: 1800-5550193</span>
        <span>tressline@mailbox.example</span>
        <span>Rosamundwigs.example</span>
        <span>48E92Avenue Harold Pinsett</span>
        <span>Larkhaven,N.Y 10990</span>
      </address>
    </section>
  </main>
</body>
</html>
```